Portfolio site - Need a basic WordPress or SquareSpace site

I need a portfolio site where I have the option to keep updating it on my own. Therefore, I'm guessing I need one that uses WordPress or SquareSpace. I just need a simple and elegant design. I'm a writer (scholarly, fiction and journalism).

Target Market(s)

Adult

Industry/Entity Type

Writer

Number of Pages Required

4 page

Font styles to use
Serif

Colors
b7a5cd
e667a6
85abd2

Requirements
Must have
• Easily updatable features. I'll have to publish links and small blurbs from time to time. And maybe the occasional image.
• Pages should be:
• Home
• Work
• Press
• Contact

```html
<!DOCTYPE html>
<html lang="en">
<head>
<meta charset="utf-8">
<title>Contact – Leona Marsh</title>
<link rel="stylesheet" href="https://fonts.googleapis.com/css2?family=Playfair+Display:ital,wght@0,400;0,700;1,400&display=swap">
<style>
:root{
  --ink:#000;
  --muted:#666;
  --soft:#999;
  --line:#dcdcdc;
  --lavender:#b7a5cd;
  --pink:#e667a6;
  --sky:#85abd2;
  --chip:#ececec;
  --serif:"Playfair Display", Georgia, serif;
}
*{box-sizing:border-box;margin:0;padding:0}
html,body{width:1141px;height:1200px;overflow:hidden;background:#fff}
body{position:relative;font-family:var(--serif);color:var(--ink)}

.site-header{position:absolute;left:0;top:0;width:1141px;height:134px;border-bottom:1px solid var(--line)}
.header-contact{position:absolute;left:119px;top:38px;list-style:none}
.header-contact li{display:flex;align-items:center;height:32px;font-style:italic;font-size:15px;color:var(--muted)}
.header-contact svg{width:14px;height:14px;margin-right:12px}
.brand{position:absolute;left:0;right:0;top:44px;text-align:center}
.brand-name{font-size:30px;font-weight:700;letter-spacing:1px}
.brand-tag{font-size:9px;color:var(--muted);letter-spacing:.5px;margin-top:-2px}
.social{position:absolute;left:843px;top:50px;display:flex;gap:17px;list-style:none}
.social li{width:37px;height:37px;border-radius:50%;background:var(--chip)}
.social li.is-accent{background:var(--sky)}

.main-nav{position:absolute;left:0;top:134px;width:1141px;height:47px;border-bottom:1px solid var(--line)}
.main-nav a{position:absolute;top:13px;transform:translateX(-50%);font-size:15px;letter-spacing:3px;color:var(--ink);text-decoration:none}
.main-nav a.is-active{color:var(--pink)}
.main-nav a.is-active::after{content:"";position:absolute;left:-4px;right:-6px;top:31px;height:3px;background:var(--pink)}

.page-title{position:absolute;left:0;right:0;top:208px;text-align:center;font-size:52px;font-weight:700;letter-spacing:1px}
.page-lede{position:absolute;left:0;right:0;top:276px;text-align:center;font-size:14px;font-style:italic}

.direct{position:absolute;left:0;right:0;display:flex;justify-content:center;align-items:center;font-weight:400}
.direct-email{top:370px;font-size:37px}
.direct-social{top:438px;font-size:27px}
.direct svg{margin-right:12px}

.divider{position:absolute;left:372px;top:575px;width:396px;display:flex;align-items:center;gap:10px;font-style:italic;font-size:14px}
.divider::before,.divider::after{content:"";flex:1;height:1px;background:var(--line)}

.contact-form{position:absolute;left:402px;top:690px;width:337px}
.form-title{text-align:center;font-size:25px;font-weight:700;margin-bottom:13px}
.field{display:block;width:337px;height:38px;margin-bottom:10px;border:1px solid var(--line);border-left:3px solid var(--ink);padding:0 18px;font-family:var(--serif);font-size:12px;color:var(--soft);background:#fff}
.field.is-focused{border-left-color:var(--pink)}
.field-message{height:130px;padding-top:12px;margin-top:2px;resize:none}
.submit{display:block;margin:12px 0 0 auto;width:146px;height:38px;border:0;background:var(--pink);color:#fff;font-family:var(--serif);font-weight:700;font-size:11px;letter-spacing:1px}

.site-footer{position:absolute;left:0;top:1151px;width:1141px;height:49px;border-top:1px solid var(--line);font-size:12px;color:var(--muted)}
.footer-nav a{position:absolute;top:15px;color:var(--muted);text-decoration:none}
.copyright{position:absolute;right:116px;top:15px}
</style>
</head>
<body>

<header class="site-header">
  <ul class="header-contact">
    <li><svg viewBox="0 0 16 16" fill="none" stroke="var(--lavender)" stroke-width="1.6"><path d="M3 2l3 3-1.5 2a8 8 0 0 0 4.5 4.5L11 10l3 3-2 2C6 15 1 10 1 4z"/></svg>hello@leonamarsh.com</li>
    <li><svg viewBox="0 0 16 12" fill="var(--lavender)"><path d="M0 0h16v12H0z"/><path d="M0 0l8 6 8-6M0 12l6-6M16 12l-6-6" stroke="#fff" stroke-width="1.2" fill="none"/></svg>(555) 014-2270</li>
  </ul>
  <div class="brand">
    <div class="brand-name">Leona Marsh</div>
    <div class="brand-tag">writer and comics scholar</div>
  </div>
  <ul class="social" aria-label="Social profiles">
    <li aria-label="Profile one"></li>
    <li class="is-accent" aria-label="Profile two"></li>
    <li aria-label="Profile three"></li>
  </ul>
</header>

<nav class="main-nav">
  <a href="#" style="left:306px">HOME</a>
  <a href="#" style="left:470px">WORK</a>
  <a href="#" style="left:636px">PRESS</a>
  <a href="#" class="is-active" style="left:818px">CONTACT</a>
</nav>

<h1 class="page-title">Contact</h1>
<p class="page-lede">You can contact Leona through email or social media.</p>

<p class="direct direct-email"><svg width="26" height="20" viewBox="0 0 26 20"><rect width="26" height="20" fill="var(--pink)"/><path d="M0 0l13 10L26 0M0 20l10-10M26 20L16 10" stroke="#fff" stroke-width="2" fill="none"/></svg>me@leonamarsh.com</p>
<p class="direct direct-social"><svg width="22" height="22" viewBox="0 0 22 22"><circle cx="11" cy="11" r="10" fill="var(--sky)"/></svg>@leonawrites</p>

<div class="divider">OR</div>

<form class="contact-form">
  <h2 class="form-title">Contact Form</h2>
  <input class="field" placeholder="Name">
  <input class="field is-focused" placeholder="Email">
  <input class="field" placeholder="Phone">
  <textarea class="field field-message" placeholder="Message"></textarea>
  <button class="submit" type="button">SUBMIT</button>
</form>

<footer class="site-footer">
  <nav class="footer-nav">
    <a href="#" style="left:193px">Home</a>
    <a href="#" style="left:265px">Work</a>
    <a href="#" style="left:333px">Press</a>
    <a href="#" style="left:402px">Contact</a>
  </nav>
  <p class="copyright">© Copyright 2018 Leona Marsh. All rights reserved.</p>
</footer>

</body>
</html>
```